CD Cover Design

Listing down some requirements:

1.Pastel color scheme (ie: baby pink, light blue, light green, pale yellow, white, silver, baby pastel purple etc.) i.e: a very sweet, dreamy and girly feel

2. Name of artist: Clara Vendt
Name of Album: Lanterns: The 1st Full Length Album
(To be added into the design of the album cover, preferably name of artist in the centre middle and name of album to be below)

Note: I wish for a feminine and classy cd cover instead of a cartoony and children-like design thankyou! Hope to not have misunderstandings because I uploaded cute graphic pictures as references! Indeed I would like the cd cover to be designed by those graphic cartoons but with a feminine and classy elegant touch instead of that like a children's album. Thank you!

3. Usage of pastel cartoon designs (like the uploaded references)

Industry/Entity Type

Baby

Font styles to use
Script

Colors
d3a5cc
b768aa
eda3c7
ecdaeb
f6f0f7
cde9f5
e9f1ce
fdf9ce

Requirements
Should not have
• Over crowding of cartoons
Ie: Don't fill the whole design with the cartoons, space them out so that it don't look so messy

```html
<!DOCTYPE html>
<html lang="en">
<head>
<meta charset="utf-8">
<title>Lanterns – CD Packaging</title>
<link rel="stylesheet" href="https://fonts.googleapis.com/css2?family=Great+Vibes&family=Parisienne&family=Arimo:wght@400&family=Courier+Prime&display=swap">
<style>
  :root {
    --board-light: #a9a9a9;
    --board-dark: #3c3c3c;
    --orchid: #b768aa;
    --orchid-soft: #d3a5cc;
    --blush: #eda3c7;
    --lilac-mist: #ecdaeb;
    --pearl: #f6f0f7;
    --sky: #cde9f5;
    --butter: #fdf9ce;
    --sun: #f4e18a;
    --hub: #6d6d70;
    --hub-ring: #8a8a8e;
    --label: #ffffff;
  }
  * { margin: 0; padding: 0; box-sizing: border-box; }
  html, body { width: 1200px; height: 900px; overflow: hidden; }
  body {
    position: relative;
    background: linear-gradient(120deg, var(--board-light) 0%, #7a7a7a 45%, var(--board-dark) 100%);
    font-family: "Arimo", sans-serif;
  }
  .panel {
    position: absolute;
    background: var(--orchid);
    overflow: hidden;
  }
  .panel--front { left: 300px; top: 27px; width: 405px; height: 405px; }
  .panel--back  { left: 726px; top: 27px; width: 438px; height: 405px; }

  .disc {
    position: absolute;
    left: 35px; top: 415px;
    width: 490px; height: 490px;
    border-radius: 50%;
    background: var(--orchid);
    overflow: hidden;
  }
  .disc__hub {
    position: absolute;
    left: 167px; top: 167px;
    width: 156px; height: 156px;
    border-radius: 50%;
    background: radial-gradient(circle, var(--hub-ring) 0 22%, var(--hub) 23% 60%, #7c7c80 61% 100%);
  }
  .disc__hole {
    position: absolute;
    left: 57px; top: 57px;
    width: 42px; height: 42px;
    border-radius: 50%;
    background: #8c8c8c;
  }

  .artist {
    position: absolute;
    font-family: "Parisienne", cursive;
    color: var(--pearl);
    white-space: nowrap;
  }
  .title {
    position: absolute;
    font-family: "Great Vibes", cursive;
    color: var(--pearl);
    white-space: nowrap;
    line-height: 1;
  }
  .subtitle {
    position: absolute;
    font-family: "Arimo", sans-serif;
    color: var(--pearl);
    white-space: nowrap;
  }

  .art {
    position: absolute;
    display: block;
  }

  .tracklist {
    position: absolute;
    left: 20px; top: 118px;
    width: 404px; height: 254px;
    border-radius: 14px;
    background: rgba(236, 218, 235, 0.42);
  }
  .tracklist__note {
    position: absolute;
    left: 27px; top: 36px;
    font-family: "Parisienne", cursive;
    font-size: 17px;
    color: var(--orchid);
  }

  .spine-text {
    position: absolute;
    font-family: "Great Vibes", cursive;
    font-size: 20px;
    color: var(--pearl);
    white-space: nowrap;
    transform-origin: left top;
  }
  .spine-text--artist { font-family: "Parisienne", cursive; font-size: 15px; }

  .view-label {
    position: absolute;
    font-family: "Courier Prime", monospace;
    font-size: 20px;
    color: var(--label);
    letter-spacing: 1px;
  }
</style>
</head>
<body>

  <!-- Front cover -->
  <section class="panel panel--front" aria-label="Front cover">
    <svg class="art" style="left:100px;top:10px" width="44" height="44" role="img" aria-label="Pastel star doodle"><circle cx="22" cy="22" r="16" fill="var(--orchid-soft)"/></svg>
    <svg class="art" style="left:165px;top:8px" width="90" height="90" role="img" aria-label="Pale yellow sun doodle"><circle cx="45" cy="45" r="38" fill="var(--sun)" opacity="0.55"/></svg>
    <svg class="art" style="left:230px;top:48px" width="56" height="56" role="img" aria-label="Moon doodle"><circle cx="28" cy="28" r="26" fill="var(--butter)" opacity="0.5"/></svg>
    <svg class="art" style="left:0;top:100px" width="40" height="40" role="img" aria-label="Pastel star doodle"><circle cx="16" cy="20" r="15" fill="var(--orchid-soft)"/></svg>
    <svg class="art" style="left:368px;top:125px" width="40" height="40" role="img" aria-label="Pastel star doodle"><circle cx="20" cy="20" r="15" fill="var(--orchid-soft)"/></svg>
    <svg class="art" style="left:0;top:155px" width="64" height="64" role="img" aria-label="Blush heart outline doodle"><circle cx="24" cy="32" r="26" fill="var(--blush)" opacity="0.45"/></svg>
    <svg class="art" style="left:313px;top:188px" width="40" height="40" role="img" aria-label="Pastel star doodle"><circle cx="20" cy="20" r="15" fill="var(--orchid-soft)"/></svg>
    <svg class="art" style="left:248px;top:240px" width="100" height="80" role="img" aria-label="Lilac masquerade mask doodle"><ellipse cx="50" cy="40" rx="46" ry="30" fill="var(--lilac-mist)" opacity="0.4"/></svg>
    <svg class="art" style="left:10px;top:235px" width="150" height="170" role="img" aria-label="Soft lilac swirl flourish"><ellipse cx="75" cy="90" rx="70" ry="78" fill="var(--orchid-soft)" opacity="0.35"/></svg>

    <p class="artist" style="left:128px;top:138px;font-size:26px">Clara Vendt</p>
    <h1 class="title" style="right:15px;top:295px;font-size:62px">Lanterns</h1>
    <p class="subtitle" style="right:24px;top:358px;font-size:15px">The 1st Full Length</p>
  </section>

  <!-- Back cover -->
  <section class="panel panel--back" aria-label="Back cover">
    <h2 class="title" style="left:48px;top:24px;font-size:32px">Lanterns</h2>
    <p class="subtitle" style="left:62px;top:63px;font-size:11px">The 1st Full Length</p>
    <svg class="art" style="left:223px;top:18px" width="90" height="90" role="img" aria-label="Pale yellow sun doodle"><circle cx="45" cy="45" r="36" fill="var(--sun)" opacity="0.55"/></svg>

    <div class="tracklist">
      <p class="tracklist__note">sample songs here</p>
      <svg class="art" style="left:62px;top:2px" width="36" height="36" role="img" aria-label="Pastel star doodle"><circle cx="18" cy="18" r="14" fill="var(--pearl)" opacity="0.5"/></svg>
      <svg class="art" style="left:200px;top:30px" width="60" height="60" role="img" aria-label="Blush heart doodle"><circle cx="30" cy="30" r="26" fill="var(--blush)" opacity="0.4"/></svg>
      <svg class="art" style="left:355px;top:28px" width="36" height="36" role="img" aria-label="Pastel star doodle"><circle cx="18" cy="18" r="14" fill="var(--pearl)" opacity="0.5"/></svg>
      <svg class="art" style="left:323px;top:88px" width="36" height="36" role="img" aria-label="Pastel star doodle"><circle cx="18" cy="18" r="14" fill="var(--pearl)" opacity="0.5"/></svg>
      <svg class="art" style="left:230px;top:120px" width="130" height="130" role="img" aria-label="Faint swirl flourish"><ellipse cx="65" cy="70" rx="60" ry="58" fill="var(--pearl)" opacity="0.2"/></svg>
    </div>

    <span class="spine-text" style="left:2px;top:165px;transform:rotate(-90deg)">Lanterns</span>
    <span class="spine-text spine-text--artist" style="left:436px;top:15px;transform:rotate(90deg)">Clara Vendt</span>
    <span class="spine-text spine-text--artist" style="left:4px;top:400px;transform:rotate(-90deg)">Clara Vendt</span>
    <span class="spine-text" style="left:436px;top:290px;transform:rotate(90deg)">Lanterns</span>

    <p class="artist" style="left:150px;top:370px;font-size:20px">Clara Vendt</p>
  </section>

  <!-- Disc face -->
  <section class="disc" aria-label="Disc face">
    <svg class="art" style="left:158px;top:40px" width="44" height="44" role="img" aria-label="Pastel star doodle"><circle cx="22" cy="22" r="16" fill="var(--orchid-soft)"/></svg>
    <svg class="art" style="left:248px;top:50px" width="90" height="90" role="img" aria-label="Pale yellow sun doodle"><circle cx="45" cy="45" r="36" fill="var(--sun)" opacity="0.55"/></svg>
    <svg class="art" style="left:65px;top:135px" width="40" height="40" role="img" aria-label="Pastel star doodle"><circle cx="20" cy="20" r="15" fill="var(--orchid-soft)"/></svg>
    <svg class="art" style="left:257px;top:115px" width="100" height="80" role="img" aria-label="Lilac masquerade mask doodle"><ellipse cx="50" cy="40" rx="46" ry="30" fill="var(--lilac-mist)" opacity="0.4"/></svg>
    <svg class="art" style="left:395px;top:160px" width="40" height="40" role="img" aria-label="Pastel star doodle"><circle cx="20" cy="20" r="15" fill="var(--orchid-soft)"/></svg>
    <svg class="art" style="left:12px;top:185px" width="64" height="64" role="img" aria-label="Blush heart outline doodle"><circle cx="32" cy="32" r="26" fill="var(--blush)" opacity="0.45"/></svg>
    <svg class="art" style="left:350px;top:212px" width="40" height="40" role="img" aria-label="Pastel star doodle"><circle cx="20" cy="20" r="15" fill="var(--orchid-soft)"/></svg>
    <svg class="art" style="left:320px;top:260px" width="56" height="56" role="img" aria-label="Moon doodle"><circle cx="28" cy="28" r="26" fill="var(--butter)" opacity="0.5"/></svg>
    <svg class="art" style="left:40px;top:265px" width="140" height="160" role="img" aria-label="Soft lilac swirl flourish"><ellipse cx="70" cy="80" rx="64" ry="74" fill="var(--orchid-soft)" opacity="0.35"/></svg>
    <svg class="art" style="left:293px;top:385px" width="40" height="40" role="img" aria-label="Pastel star doodle"><circle cx="20" cy="20" r="15" fill="var(--orchid-soft)"/></svg>

    <div class="disc__hub"><div class="disc__hole"></div></div>

    <p class="artist" style="left:180px;top:115px;font-size:25px">Clara Vendt</p>
    <h2 class="title" style="left:130px;top:305px;font-size:62px">Lanterns:</h2>
    <p class="subtitle" style="left:180px;top:370px;font-size:15px">The 1st Full Length</p>
  </section>

  <p class="view-label" style="left:482px;top:448px">FRONT</p>
  <p class="view-label" style="left:920px;top:451px">BACK</p>
  <p class="view-label" style="left:505px;top:799px">CD</p>

</body>
</html>
```